Business Card Design

WE are looking for a premium quality Business Cards for a Law Firm . Copies of our current business card is attached.

Contact Information for Business Card

xyz

```html
<!DOCTYPE html>
<html lang="en">
<head>
<meta charset="utf-8">
<title>Harrowgate Lawyers – Business Card</title>
<link href="https://fonts.googleapis.com/css2?family=EB+Garamond:wght@400;500&family=Lato:wght@400;700&display=swap" rel="stylesheet">
<style>
  :root {
    --stage: #2b2d30;
    --card-green: #0f2a1e;
    --card-green-deep: #0a2016;
    --gold: #c9a15c;
    --gold-soft: #b8914f;
    --ivory: #e9e4d8;
    --watermark: rgba(201, 161, 92, 0.10);
  }
  * { margin: 0; padding: 0; box-sizing: border-box; }
  html, body { width: 1200px; height: 952px; overflow: hidden; }
  body {
    background: var(--stage);
    position: relative;
    font-family: "EB Garamond", serif;
  }
  .card {
    position: absolute;
    top: 322px;
    width: 540px;
    height: 308px;
    border-radius: 22px;
    background: linear-gradient(160deg, var(--card-green) 0%, var(--card-green-deep) 100%);
    overflow: hidden;
    box-shadow: 0 14px 30px rgba(0,0,0,0.45);
  }
  .card--front { left: 50px; }
  .card--back { left: 610px; }

  /* Front */
  .brand {
    position: absolute;
    left: 40px;
    top: 34px;
    width: 190px;
    text-align: center;
    color: var(--gold);
  }
  .brand__mark {
    width: 30px; height: 30px;
    border: 2px solid var(--gold);
    border-radius: 50%;
    margin: 0 auto 8px;
  }
  .brand__name {
    font-size: 28px;
    font-weight: 500;
    letter-spacing: 1px;
    line-height: 1;
  }
  .brand__sub {
    display: flex;
    align-items: center;
    gap: 8px;
    margin-top: 4px;
    font-size: 11px;
    font-weight: 500;
    letter-spacing: 6px;
  }
  .brand__sub::before, .brand__sub::after {
    content: ""; flex: 1; height: 1px; background: var(--gold-soft);
  }
  .contacts {
    position: absolute;
    left: 30px;
    top: 170px;
    list-style: none;
    color: var(--ivory);
    font-size: 14px;
    z-index: 1;
  }
  .contacts li {
    display: flex;
    align-items: center;
    gap: 9px;
    height: 22px;
  }
  .contacts__icon {
    width: 15px; height: 15px;
    border-radius: 3px;
    background: var(--gold);
    display: flex; align-items: center; justify-content: center;
  }
  .watermark {
    position: absolute;
    left: 170px;
    top: 190px;
    width: 240px; height: 240px;
    border: 5px solid var(--watermark);
    border-radius: 50%;
  }
  .holder {
    position: absolute;
    right: 30px;
    top: 168px;
    text-align: right;
    font-family: "Lato", sans-serif;
    z-index: 1;
  }
  .holder__name {
    color: var(--gold);
    font-weight: 700;
    font-size: 24px;
    letter-spacing: 0.5px;
  }
  .holder__title, .holder__cred {
    color: var(--ivory);
    font-size: 11.5px;
    line-height: 1.35;
  }
  .holder__title { font-weight: 700; letter-spacing: 0.3px; }

  /* Back */
  .back-layout {
    position: absolute;
    inset: 0;
    display: flex;
    align-items: center;
    justify-content: center;
    gap: 26px;
  }
  .address {
    color: var(--gold);
    font-size: 13px;
    text-align: center;
    line-height: 1.35;
    padding: 6px 0;
    border-top: 1px solid var(--gold-soft);
    border-bottom: 1px solid var(--gold-soft);
  }
  .back-brand {
    display: flex;
    align-items: center;
    gap: 10px;
    color: var(--gold);
  }
  .back-brand__mark {
    width: 34px; height: 34px;
    border: 2px solid var(--gold);
    border-radius: 50%;
  }
  .back-brand__name {
    font-size: 24px;
    font-weight: 500;
    letter-spacing: 1px;
  }
</style>
</head>
<body>

<section class="card card--front">
  <div class="watermark" aria-hidden="true"></div>

  <div class="brand">
    <div class="brand__mark"></div>
    <div class="brand__name">HARROWGATE</div>
    <div class="brand__sub">LAWYERS</div>
  </div>

  <ul class="contacts">
    <li>
      <span class="contacts__icon">
        <svg width="9" height="9" viewBox="0 0 10 10"><path d="M2 1 L4 1 L4.6 3.2 L3.4 4 Q4.3 5.9 6 6.6 L6.8 5.4 L9 6 L9 8 Q9 9 8 9 Q1 8.5 1 2 Q1 1 2 1Z" fill="#0f2a1e"/></svg>
      </span>+61 7 3000 1248
    </li>
    <li>
      <span class="contacts__icon">
        <svg width="9" height="9" viewBox="0 0 10 10"><rect x="2.5" y="0.8" width="5" height="8.4" rx="1" fill="#0f2a1e"/><rect x="3.4" y="1.9" width="3.2" height="5" fill="#c9a15c"/></svg>
      </span>+61 0400 917 362
    </li>
    <li>
      <span class="contacts__icon">
        <svg width="9" height="9" viewBox="0 0 10 10"><rect x="0.8" y="2" width="8.4" height="6" rx="0.8" fill="#0f2a1e"/><path d="M1.2 2.5 L5 5.4 L8.8 2.5" stroke="#c9a15c" stroke-width="0.9" fill="none"/></svg>
      </span>daniel@harrowgatelawyers.com.au
    </li>
    <li>
      <span class="contacts__icon">
        <svg width="9" height="9" viewBox="0 0 10 10"><circle cx="5" cy="5" r="4" fill="none" stroke="#0f2a1e" stroke-width="1.1"/><ellipse cx="5" cy="5" rx="1.7" ry="4" fill="none" stroke="#0f2a1e" stroke-width="0.9"/><line x1="1" y1="5" x2="9" y2="5" stroke="#0f2a1e" stroke-width="0.9"/></svg>
      </span>www.harrowgatelawyers.com.au
    </li>
  </ul>

  <div class="holder">
    <div class="holder__name">DANIEL MERCER</div>
    <div class="holder__title">DIRECTOR &amp; PRINCIPAL SOLICITOR</div>
    <div class="holder__cred">MBA, Juris Doctor</div>
  </div>
</section>

<section class="card card--back">
  <div class="back-layout">
    <div class="address">
      Suite 12, Harrowgate House, 42 Harrow Terrace<br>
      Ashcombe Vale, NSW 2999
    </div>
    <div class="back-brand">
      <div class="back-brand__mark"></div>
      <div class="back-brand__name">HARROWGATE</div>
    </div>
  </div>
</section>

</body>
</html>
```